Free Shipping on Orders of $50 and Over

Ideally, I would like a HTML5 banner for the homepage of https://www.quillmarrowhome.com showing free shipping for orders of $50 or more. If there are some ways to make it with moving elements, like something using HTML5, that would be better.

The theme on the site using WP Bakery (Wordpress) and can be built with that plugin, or with HTML5 or a simple jpg.
Updates

To clarify, it does not have to be in HTML5. I would like some animation but it is not mandatory. Video or gif is okay too,.

Industry/Entity Type

Home And Garden

Font styles to use
Sans Serif

Requirements
Must have
• orders $50 or more
domestic usa only
Nice to have
• something that moves. Would be great if I could use this same banner through black Friday, Cyber Monday, etc.
Should not have
• colors that clash with current website colors

```html
<!DOCTYPE html>
<html lang="en">
<head>
<meta charset="utf-8">
<title>Free Shipping on Orders of $50 or More</title>
<link href="https://fonts.googleapis.com/css2?family=Nunito+Sans:wght@400;800;900&display=swap" rel="stylesheet">
<style>
  :root {
    --bg: #ffffff;
    --ink: #2b2b2b;
    --accent-red: #e8413c;
    --tone-royal: #1a36d8;
    --tone-sky: #0a8ecf;
    --tone-indigo: #2e3190;
    --tone-navy: #130f8e;
  }
  html, body {
    margin: 0;
    padding: 0;
    overflow: hidden;
    background: var(--bg);
  }
  .banner {
    position: relative;
    width: 1200px;
    height: 309px;
    overflow: hidden;
    background: var(--bg);
    font-family: "Nunito Sans", sans-serif;
  }
  .banner__accent {
    position: absolute;
    top: 0;
    height: 309px;
  }
  .banner__accent--left {
    left: 0;
    width: 240px;
    border-bottom-right-radius: 120px;
    background: linear-gradient(160deg, var(--tone-royal) 0%, var(--tone-royal) 40%, var(--tone-sky) 100%);
  }
  .banner__accent--right {
    right: 0;
    width: 250px;
    border-top-left-radius: 120px;
    background: linear-gradient(200deg, var(--tone-indigo) 0%, var(--tone-indigo) 40%, var(--tone-navy) 100%);
  }

  .banner__headline {
    position: absolute;
    left: 0;
    width: 1200px;
    top: 78px;
    margin: 0;
    text-align: center;
    color: var(--ink);
    font-weight: 900;
    font-size: 72px;
    line-height: 1;
    letter-spacing: 0.055em;
  }
  .banner__offer {
    position: absolute;
    left: 18px;
    width: 1200px;
    top: 164px;
    margin: 0;
    text-align: center;
    color: var(--ink);
    font-weight: 400;
    font-size: 46px;
    line-height: 1;
    letter-spacing: 0.01em;
  }
  .banner__note {
    position: absolute;
    left: 0;
    width: 1200px;
    top: 254px;
    margin: 0;
    text-align: center;
    color: var(--accent-red);
    font-weight: 400;
    font-size: 26px;
    line-height: 1;
  }
</style>
</head>
<body>
  <section class="banner" aria-label="Free shipping promotion">
    <div class="banner__accent banner__accent--left" role="img" aria-label="Decorative abstract shapes in royal and sky blue"></div>
    <div class="banner__accent banner__accent--right" role="img" aria-label="Decorative abstract shapes in indigo and navy"></div>
    <h1 class="banner__headline">FREE SHIPPING</h1>
    <p class="banner__offer">for orders of $50 or more</p>
    <p class="banner__note">*domestic USA only</p>
  </section>
</body>
</html>
```